Flyer Design Project

A beauty salon Velmora Spa needs a flyer design to promote some new services that are available in the salon. These are anti-aging, slimming and other treatments performed on the modern high-tech cosmetological equipment.
The flyer will be distrubuted in hi-end supermarket located near the salon. It would go inside the bags when the purchases are packed at the cashier desk.
The main idea is make people read it and not to throw it away immediately. The flyer will be printed on the top quality paper.
There will either be a discound or a promotional treatment in the flyer.
We are not sure about the size of the flyer. It should not be too big neither too small. Ideally on the one side there should be information about Facial Treatments and on the other about the Body Treatments. However we are open for other suggestions of the Pixel Harbor.
This is our web-site www.velmora-spa.ru
Though being in Russian, it may give you an idea of our concept.
Updates

Thanks for all the designs submitted.

One general comment would be - the flyer should look different from the usual flyer one might get regarding the beauty salon services. Please make it attractive and unusual. Thanks.

Target Market(s)

Ladies from 25 to 60 years old who are well-to-do

Industry/Entity Type

Beauty Salon

Requirements
Nice to have
• It would be nice to have some technical features in the design.
Should not have
• The flyer should not be overloaded with pictures or graphic design features. It should be elegant and clear. The design should not look too "spa" as we promote technological treatments not massages.

```html
<!DOCTYPE html>
<html lang="en">
<head>
<meta charset="utf-8">
<title>Velmora Spa — Facials 20% Off</title>
<link rel="stylesheet" href="https://fonts.googleapis.com/css2?family=Questrial&display=swap">
<style>
  :root {
    --bg-maroon: #3e1b1b;
    --motif-tone: #452020;
    --text-light: #ffffff;
  }
  * { margin: 0; padding: 0; box-sizing: border-box; }
  html, body {
    width: 779px;
    height: 1200px;
    overflow: hidden;
    background: var(--bg-maroon);
  }
  .flyer {
    position: relative;
    width: 779px;
    height: 1200px;
    background: var(--bg-maroon);
    color: var(--text-light);
    font-family: "Questrial", sans-serif;
    text-align: center;
    overflow: hidden;
  }
  .flyer__motif {
    position: absolute;
    inset: 0;
    background: radial-gradient(ellipse at 50% 45%, var(--motif-tone) 0%, var(--bg-maroon) 75%);
  }
  .flyer__content { position: relative; }
  .headline {
    position: absolute;
    left: 0; right: 0;
    top: 66px;
    font-size: 118px;
    line-height: 1;
    font-weight: 400;
    letter-spacing: 1px;
  }
  .services {
    position: absolute;
    left: 0; right: 0;
    top: 228px;
    font-size: 41px;
    line-height: 54px;
    list-style: none;
  }
  .offer {
    position: absolute;
    left: 0; right: 0;
    top: 535px;
    font-size: 138px;
    line-height: 110px;
    letter-spacing: -2px;
  }
  .brand {
    position: absolute;
    left: 0; right: 0;
    top: 1030px;
    display: flex;
    justify-content: center;
    align-items: center;
    gap: 14px;
  }
  .brand__dot {
    width: 30px; height: 30px;
    border-radius: 50%;
    background: var(--text-light);
  }
  .brand__name {
    font-size: 44px;
    line-height: 1;
  }
  .brand__tagline {
    font-size: 19px;
    line-height: 22px;
    text-align: left;
    margin-left: 8px;
  }
  .website {
    position: absolute;
    left: 0; right: 0;
    top: 1146px;
    font-size: 21px;
    letter-spacing: 0.5px;
  }
</style>
</head>
<body>
  <main class="flyer">
    <div class="flyer__motif" role="img" aria-label="Faint repeating decorative motif across the background"></div>
    <div class="flyer__content">
      <h1 class="headline">facials</h1>
      <ul class="services">
        <li>cosmetology</li>
        <li>anti ageing</li>
      </ul>
      <p class="offer">20%<br>OFF</p>
      <div class="brand">
        <span class="brand__dot"></span>
        <span class="brand__name">Velmora Spa</span>
        <span class="brand__tagline" lang="ru">салон<br>красоты</span>
      </div>
      <p class="website">www.velmora-spa.ru</p>
    </div>
  </main>
</body>
</html>
```